Small but growing painting company. Have built up a steady client base. Want to start having a more professional look. Want to start with changing my business cards, and also getting new logo and tee shirts.

Target Market(s)

Home owners, property management companies, all ages 30-70

Industry/Entity Type

Painting And Decorating

Contact Information for Business Card

Bright Ridge Painting LLC Derek Vanstrand 630-485-7039 interior, exterior, vaulted ceiling, drywall repair, pressure washing, kitchen cabinets, epoxy, garage floors,

Font styles to use
Sans Serif
Other font styles liked:
• Harrington

Colors
0355a3
ffffff
ec1f27
000000
3176b5
0493ce
474747
b7b7b7

Requirements
Must have
• Creative, something that doesn’t look like every other painting card.
Nice to have
• I would like something with an arrow or something going to a point

```html
<!DOCTYPE html>
<html lang="en">
<head>
<meta charset="utf-8">
<title>Bright Ridge Painting LLC — Business Cards</title>
<link rel="stylesheet" href="https://fonts.googleapis.com/css2?family=Oswald:wght@500&family=Lato:wght@400&display=swap">
<style>
  :root {
    --stage: #1b1b1b;
    --card-light: #f3f3f3;
    --brand-red: #ec1f27;
    --ink: #2b2b2b;
    --white: #ffffff;
  }
  * { margin: 0; padding: 0; box-sizing: border-box; }
  html, body { width: 1200px; height: 900px; overflow: hidden; }
  body { background: var(--stage); position: relative; font-family: "Lato", sans-serif; }

  .card {
    position: absolute;
    top: 200px;
    width: 310px;
    height: 502px;
    box-shadow: 3px 4px 6px rgba(0,0,0,0.55);
  }
  .card--front {
    left: 253px;
    background: var(--card-light);
    border-radius: 62px 0 62px 0;
  }
  .card--back {
    left: 627px;
    background: var(--brand-red);
    border-radius: 0 62px 0 62px;
  }

  .brand-mark {
    position: absolute;
    left: 50%;
    top: 68px;
    width: 134px;
    height: 134px;
    margin-left: -67px;
    border-radius: 50%;
  }
  .card--front .brand-mark { background: var(--brand-red); }
  .card--back .brand-mark { background: var(--white); }

  .brand-name {
    position: absolute;
    left: 0;
    right: 0;
    top: 212px;
    text-align: center;
    font-family: "Oswald", sans-serif;
    font-weight: 500;
    font-size: 24px;
    line-height: 1.2;
    letter-spacing: 0.2px;
  }
  .card--front .brand-name { color: var(--ink); }
  .card--back .brand-name { color: var(--white); }

  .contact {
    position: absolute;
    left: 32px;
    top: 322px;
    color: var(--ink);
  }
  .contact__name {
    font-family: "Oswald", sans-serif;
    font-weight: 500;
    font-size: 21px;
    color: var(--brand-red);
    line-height: 1.2;
    margin-bottom: 8px;
  }
  .contact__line {
    display: flex;
    align-items: center;
    gap: 4px;
    font-size: 14.5px;
    line-height: 18px;
  }
  .contact__line svg { width: 13px; height: 13px; flex: none; }
  .contact__address {
    margin-top: 8px;
    font-size: 14.5px;
    line-height: 19px;
  }

  .services {
    position: absolute;
    left: 32px;
    top: 330px;
    list-style: none;
    color: var(--white);
    font-size: 14.5px;
    line-height: 18.2px;
  }
  .services li { position: relative; padding-left: 11px; }
  .services li::before {
    content: "";
    position: absolute;
    left: 0;
    top: 6px;
    width: 6px;
    height: 6px;
    border-radius: 50%;
    background: var(--white);
  }
</style>
</head>
<body>

  <section class="card card--front" aria-label="Business card front">
    <div class="brand-mark" aria-hidden="true"></div>
    <p class="brand-name">BRIGHT RIDGE PAINTING LLC</p>

    <div class="contact">
      <p class="contact__name">DEREK VANSTRAND</p>
      <p class="contact__line">
        <svg viewBox="0 0 16 16" aria-hidden="true"><path fill="#ec1f27" d="M3 2h3l1.5 3.5-2 1.2a8 8 0 0 0 3.8 3.8l1.2-2L14 10v3a1 1 0 0 1-1 1A11 11 0 0 1 2 3a1 1 0 0 1 1-1z"/></svg>
        630-485-7039
      </p>
      <p class="contact__line">
        <svg viewBox="0 0 16 16" aria-hidden="true"><rect x="1" y="3" width="14" height="10" fill="#ec1f27"/><path d="M1.5 3.5 8 9l6.5-5.5" fill="none" stroke="#f3f3f3" stroke-width="1.3"/></svg>
        hello@brightridgepaint.com
      </p>
      <p class="contact__line">
        <svg viewBox="0 0 16 16" aria-hidden="true"><circle cx="8" cy="8" r="7" fill="#ec1f27"/><path d="M1 8h14M8 1c-3 3.5-3 10.5 0 14M8 1c3 3.5 3 10.5 0 14" fill="none" stroke="#f3f3f3" stroke-width="1"/></svg>
        www.brightridgepaint.com
      </p>
      <p class="contact__address">78 Maple Crest Road,<br>Naperville, IL 60540</p>
    </div>
  </section>

  <section class="card card--back" aria-label="Business card back">
    <div class="brand-mark" aria-hidden="true"></div>
    <p class="brand-name">BRIGHT RIDGE PAINTING LLC</p>

    <ul class="services">
      <li>Interior, Exterior</li>
      <li>Vaulted Ceiling</li>
      <li>Drywall Repair</li>
      <li>Pressure Washing</li>
      <li>Kitchen Cabinets</li>
      <li>Epoxy</li>
      <li>Garage Floors.</li>
    </ul>
  </section>

</body>
</html>
```